Tidewell Recovery Business Card Design

Professional and clean design. The design colors should flow with the logo. Two-sided card with the website on the back which is:

www.TidewellRecovery.example.

"Specializing in Water Damage Restoration"

On the front I need the name, email, phone, and logo.

Name: Dorian Vashti
Email: Dorian@TidewellRecovery.example
Phone: 555-318-2046 for now

I only have the Preview and Thumbnail right now but should have the source files uploaded within a day or two.

Target Market(s)

Flood victims, home owners with water damage from busted pipes etc...

Industry/Entity Type

Business

Contact Information for Business Card

Name: Dorian Vashti

Font styles to use
Serif
Sans Serif

```html
<!DOCTYPE html>
<html lang="en">
<head>
<meta charset="utf-8">
<title>Tidewell Recovery Business Card</title>
<link rel="stylesheet" href="https://fonts.googleapis.com/css2?family=Cinzel:wght@500&family=Source+Sans+3:ital,wght@0,400;0,600;1,600&display=swap">
<style>
  :root {
    --backdrop: #3b3b3b;
    --card-light: #f7f8f9;
    --card-dark: #000000;
    --brand-blue: #2b8fd3;
    --brand-faint: #e3eff8;
    --text-gray: #4a4a4a;
    --white: #ffffff;
  }
  html, body {
    margin: 0;
    width: 1200px;
    height: 750px;
    overflow: hidden;
    background: var(--backdrop);
  }
  .stage { position: relative; width: 1200px; height: 750px; }
  .card {
    position: absolute;
    top: 228px;
    width: 461px;
    height: 262px;
    overflow: hidden;
  }
  .card--front { left: 124px; background: var(--card-light); }
  .card--back { left: 618px; background: var(--card-dark); }

  .front-decor {
    position: absolute;
    right: -70px;
    top: -10px;
    width: 270px;
    height: 270px;
    border-radius: 50%;
    background: var(--brand-faint);
  }
  .brand {
    position: absolute;
    text-align: center;
    font-family: "Cinzel", serif;
    font-weight: 500;
    letter-spacing: 1px;
    line-height: 1.1;
  }
  .brand__mark {
    display: block;
    margin: 0 auto 10px;
    border-radius: 50%;
  }
  .card--front .brand {
    left: 24px; top: 32px; width: 180px;
    color: var(--brand-blue); font-size: 20px;
  }
  .card--front .brand__mark { width: 52px; height: 52px; background: var(--brand-blue); }

  .holder-name {
    position: absolute;
    right: 25px; top: 91px;
    margin: 0;
    font-family: "Source Sans 3", sans-serif;
    font-weight: 600;
    font-size: 17px;
    color: var(--brand-blue);
  }
  .name-rule {
    position: absolute;
    left: 196px; right: 25px; top: 122px;
    height: 1.5px;
    background: var(--brand-blue);
  }
  .contact {
    position: absolute;
    left: 31px; top: 182px;
    margin: 0; padding: 0;
    list-style: none;
    font-family: "Source Sans 3", sans-serif;
    font-size: 13px;
    color: var(--text-gray);
  }
  .contact li { display: flex; align-items: center; height: 17.5px; }
  .contact svg { width: 11px; height: 11px; margin-right: 6px; fill: var(--brand-blue); }

  .card--back .brand {
    left: 0; right: 0; top: 68px;
    color: var(--white); font-size: 26px;
  }
  .card--back .brand__mark { width: 64px; height: 64px; background: var(--white); margin-bottom: 12px; }
  .tagline {
    position: absolute;
    left: 0; right: 0; top: 224px;
    margin: 0;
    text-align: center;
    font-family: "Source Sans 3", sans-serif;
    font-style: italic;
    font-weight: 600;
    font-size: 14px;
    color: var(--white);
  }
</style>
</head>
<body>
<main class="stage">
  <section class="card card--front">
    <div class="front-decor"></div>
    <div class="brand">
      <span class="brand__mark"></span>
      TIDEWELL<br>RECOVERY
    </div>
    <h1 class="holder-name">Dorian Vashti</h1>
    <div class="name-rule"></div>
    <ul class="contact">
      <li>
        <svg viewBox="0 0 24 24" aria-hidden="true"><path d="M6.6 10.8a15.2 15.2 0 0 0 6.6 6.6l2.2-2.2a1 1 0 0 1 1-.25 11.4 11.4 0 0 0 3.6.57 1 1 0 0 1 1 1V20a1 1 0 0 1-1 1A17 17 0 0 1 3 4a1 1 0 0 1 1-1h3.5a1 1 0 0 1 1 1c0 1.25.2 2.45.57 3.57a1 1 0 0 1-.25 1z"/></svg>
        555-318-2046 for now
      </li>
      <li>
        <svg viewBox="0 0 24 24" aria-hidden="true"><path d="M2 5h20v14H2z M3.5 6.5 12 13l8.5-6.5" fill="var(--brand-blue)" stroke="var(--card-light)" stroke-width="1.5"/></svg>
        Dorian@TidewellRecovery.example
      </li>
      <li>
        <svg viewBox="0 0 24 24" aria-hidden="true"><circle cx="12" cy="12" r="10"/></svg>
        TidewellRecovery.example
      </li>
    </ul>
  </section>

  <section class="card card--back">
    <div class="brand">
      <span class="brand__mark"></span>
      TIDEWELL<br>RECOVERY
    </div>
    <p class="tagline">Specializing in Water Damage Restoration</p>
  </section>
</main>
</body>
</html>
```